Runners Report - 2 page freshen up from previous design

We need a report design to display information for runners in an easy to read - almost like an infographic format. Our software collect data on someones running style and gives us information based on this in the form of numbers. We then compare it to a database and display it back in a range of low, ideal, or, excessive. The purpose of the report is to give to the client after their running gait analysis assessment to help them better to understand their results ( which are currently very complicated). I would like to see the final design with simliar formats of the biomechanical man pictures ( currently i've used different ones for examples). I have shown an example of what im looking for, and i basically need it tidied up and made to look more professional. Our colours are navy blue, red, and white. I would be happy to see some options with a white background as well.

Needed:
2 page report:
First page is the running gait analysis information
Second page is strength flexibiltiy, structural and functional information
Data needs to be inputted and changed in these files everytime
I want it to look professional, but also a bit flashy ( or 'cool') and easy to read.

Target Market(s)

Runners , Triathletes, Sports people

Industry/Entity Type

Health And Wellness

Font styles to use
Serif
Sans Serif

Colors
0455a3
ec1f27
ffffff

Requirements
Must have
• All of the information I've given in my example.
• Must have a graph format with traffic light system for the parameters with Pelvis/hip/knee/ankle.
• Must have biomechanical men - 3D men running etc all in the same format/ design
• Must be able to input different data each time to change the results
• Must have Velk9 logo
Nice to have
• Different options - dark blue or white background?
Should not have
• cartoons or unrealistic figures

```html
<!DOCTYPE html>
<html lang="en">
<head>
<meta charset="utf-8">
<title>Velk9 Runner Report</title>
<link rel="stylesheet" href="https://fonts.googleapis.com/css2?family=Noto+Serif:wght@400&family=Open+Sans:wght@400;600;700;800&display=swap">
<style>
:root{
  --navy:#15285b;
  --navy-deep:#0c1b44;
  --blue:#0455a3;
  --blue-bright:#1a6fd0;
  --red:#ec1f27;
  --red-deep:#c4141b;
  --white:#ffffff;
  --ink:#1b2a4e;
  --grey-bg:#e2e2e2;
  --green:#2db34a;
  --yellow:#f5e11d;
  --orange:#f39a1e;
  --skin:#e7c9a7;
}
*{box-sizing:border-box;margin:0;padding:0}
html,body{width:1200px;height:858px;overflow:hidden}
body{background:var(--grey-bg);font-family:"Open Sans",Arial,sans-serif;position:relative;color:var(--white)}
.page-caption{position:absolute;top:36px;width:500px;text-align:center;font-family:"Noto Serif",Georgia,serif;font-size:19px;letter-spacing:.5px;color:#222}
.page-caption--front{left:78px}
.page-caption--back{left:622px}

.page{position:absolute;top:79px;width:500px;height:707px;overflow:hidden;
  background:radial-gradient(ellipse at 50% 30%,#1d3470 0%,var(--navy) 55%,var(--navy-deep) 100%);
  box-shadow:0 6px 18px rgba(0,0,0,.25)}
.page--front{left:78px}
.page--back{left:622px}
.page::after{content:"";position:absolute;right:0;bottom:0;width:100px;height:7px;background:var(--red);clip-path:polygon(8% 0,100% 0,100% 100%,0 100%)}

.header{position:absolute;left:0;top:0;width:100%;height:72px;
  background:linear-gradient(100deg,#0a2566 0%,#13429a 45%,#0d2c78 100%)}
.header::before{content:"";position:absolute;right:0;top:26px;width:90px;height:2px;background:var(--red);box-shadow:0 8px 0 rgba(255,255,255,.35),0 16px 0 var(--red)}
.brand{position:absolute;font-weight:800;color:var(--white);letter-spacing:.5px}
.page--front .brand{left:16px;top:22px;font-size:21px}
.page--back .brand{left:0;width:100%;text-align:center;top:16px;font-size:30px}
.report-title{position:absolute;left:112px;top:8px;font-size:40px;font-weight:600;line-height:56px}
.name-band{position:absolute;left:0;top:72px;width:100%;height:32px;background:var(--red);
  text-align:center;font-weight:700;font-size:18px;line-height:32px;letter-spacing:.3px}

.side-legend{position:absolute;font-size:4px;line-height:6px;text-align:right;color:#cdd6ea}
.side-legend i{display:inline-block;width:4px;height:4px;margin-left:2px;vertical-align:middle}
.side-legend .r{background:var(--red)}
.side-legend .l{background:var(--blue-bright)}

.section-tab{position:absolute;top:133px;height:18px;width:118px;background:var(--white);border-radius:9px 0 0 9px;
  color:var(--red);font-size:9.5px;line-height:18px;padding-left:30px}
.section-tab b{position:absolute;left:0;top:-1px;width:20px;height:20px;border-radius:50%;border:2px solid var(--red);background:var(--white);
  color:var(--red);text-align:center;line-height:16px;font-size:10px;font-weight:700}
.section-tab::after{content:"";position:absolute;left:118px;top:0;width:38px;height:18px;
  background:repeating-linear-gradient(120deg,var(--blue-bright) 0 4px,transparent 4px 8px)}
.runner-figure{position:absolute;width:36px;height:44px;border-radius:4px;
  background:linear-gradient(180deg,rgba(255,255,255,.75),rgba(236,31,39,.5))}
.field{position:absolute;font-size:7.5px;color:var(--white)}
.checkbox{display:inline-block;width:9px;height:9px;background:var(--white);border:1px solid var(--red);vertical-align:middle;margin-right:5px}

.bio-table{position:absolute;left:15px;top:206px;width:470px;height:280px;background:var(--white);border-radius:3px;overflow:hidden}
.bio-table__head{position:absolute;left:0;top:0;width:100%;height:18px;background:var(--red)}
.plane-title{position:absolute;top:0;height:18px;line-height:18px;text-align:center;font-size:8px}
.plane-divider{position:absolute;top:0;bottom:0;width:0;border-left:1px dashed #b9c0cf}
.joint{position:absolute;left:0;width:150px;height:52px}
.joint__photo{position:absolute;left:9px;top:0;width:52px;height:52px;border-radius:50%;border:3px solid var(--ink);
  background:radial-gradient(circle at 45% 40%,#fbf1e4,var(--skin) 70%,#c99c72);z-index:2}
.joint__tab{position:absolute;left:35px;top:17px;width:102px;height:19px;background:var(--ink);color:var(--white);
  font-weight:700;font-size:10px;line-height:19px;padding-left:32px}
.joint__tab::after{content:"";position:absolute;right:0;top:0;width:26px;height:19px;
  background:repeating-linear-gradient(120deg,var(--white) 0 2px,transparent 2px 6px)}
.gauge{position:absolute;width:104px;text-align:center}
.gauge__label{font-size:6.2px;color:var(--ink);height:10px;line-height:10px;text-transform:uppercase}
.gauge svg{display:block;margin:5px auto 0;width:66px;height:38px}

.ribbon{position:absolute;height:21px;line-height:21px;text-align:center;font-size:9.5px;color:var(--white);z-index:3}
.ribbon::before{content:"";position:absolute;left:-10px;right:-10px;top:-2px;bottom:-2px;background:var(--red);opacity:.55;
  clip-path:polygon(0 50%,12px 0,16px 0,4px 50%,16px 100%,12px 100%,0 50%,100% 50%,calc(100% - 12px) 0,calc(100% - 16px) 0,calc(100% - 4px) 50%,calc(100% - 16px) 100%,calc(100% - 12px) 100%,100% 50%)}
.ribbon::after{content:"";position:absolute;inset:0;background:linear-gradient(180deg,#f2383f,var(--red-deep));z-index:-1;
  clip-path:polygon(10px 0,calc(100% - 10px) 0,100% 50%,calc(100% - 10px) 100%,10px 100%,0 50%)}

.track{position:absolute;height:3px;border-radius:2px}
.track--blue{background:var(--blue-bright)}
.track--stride{background:linear-gradient(90deg,var(--green),var(--yellow) 50%,var(--red))}
.track--width{background:linear-gradient(90deg,var(--red),var(--yellow) 30%,var(--green) 50%,var(--yellow) 70%,var(--red))}
.track--bridge{height:5px;background:linear-gradient(90deg,var(--red),var(--orange) 30%,var(--yellow) 55%,var(--green))}
.tick{position:absolute;width:1px;height:9px;background:#8ea4d1;top:-3px}
.marker{position:absolute;width:12px;height:12px;border-radius:50%;border:1px solid var(--white);
  font-size:6px;font-weight:700;line-height:10px;text-align:center;color:var(--white);transform:translate(-50%,-50%)}
.marker--l{background:var(--blue-bright)}
.marker--r{background:var(--red)}
.knob{position:absolute;width:13px;height:13px;border-radius:50%;transform:translate(-50%,-50%);
  background:radial-gradient(circle,#fff,#bfc4cc);border:1px solid #8a8f99}
.knob::after{content:"";position:absolute;left:3px;top:3px;width:5px;height:5px;
  background:repeating-linear-gradient(90deg,#666 0 1px,transparent 1px 2px)}
.scale-text{position:absolute;font-size:7px;color:var(--white);transform:translateX(-50%);white-space:nowrap}
.foot-photo{position:absolute;width:34px;height:34px;border-radius:50%;border:2px solid #c8d1e6;
  background:radial-gradient(circle at 50% 45%,#fff,#f0d6bc 70%,#d6a97f)}

.vertical-bar{position:absolute;left:27px;top:605px;width:5px;height:85px;background:linear-gradient(180deg,var(--red),var(--yellow) 50%,var(--green))}
.vertical-bar::before,.vertical-bar::after{content:"";position:absolute;left:-7px;width:19px;height:2px;background:#d9dfee}
.vertical-bar::before{top:-1px}.vertical-bar::after{bottom:-1px}
.round-arrow{position:absolute;width:14px;height:14px;border-radius:50%;background:var(--red)}
.round-arrow svg{display:block;width:14px;height:14px}
.cadence-value{position:absolute;left:134px;top:602px;width:120px;text-align:center;font-size:31px;font-weight:700;line-height:36px}
.cadence-unit{position:absolute;left:134px;top:637px;width:120px;text-align:center;font-size:6px}
.good-pill{position:absolute;left:186px;top:684px;width:16px;height:5px;border-radius:3px;background:var(--green);font-size:3.5px;line-height:5px;text-align:center}

.scale-panel{position:absolute;left:35px;width:427px;height:165px;background:var(--white)}
.scale-panel__key{position:absolute;top:20px;font-size:8px}
.key-weak{left:95px;color:var(--red)}
.key-avg{left:234px;color:#e3b81c}
.key-strong{right:14px;color:var(--green);font-weight:600}
.scale-row{position:absolute;left:0;width:100%;height:12px}
.scale-row__name{position:absolute;left:23px;top:0;font-size:7px;color:var(--ink);line-height:12px}
.scale-row__bar{position:absolute;left:95px;top:3px;width:307px;height:6px;
  background:linear-gradient(90deg,var(--red),var(--orange) 28%,var(--yellow) 50%,#9fd23b 72%,var(--green))}
.scale-row .marker{top:3px}
.scale-row .marker--l{background:var(--ink)}

.score-pill{position:absolute;width:30px;height:12px;border-radius:6px;font-size:7px;line-height:12px;text-align:center;transform:translateX(-50%)}
.score-pill--right{background:var(--red)}
.score-pill--left{background:var(--blue-bright)}
.score{position:absolute;font-size:32px;font-weight:600;line-height:36px;transform:translateX(-50%)}
.fault-list{position:absolute;left:27px;top:587px;width:200px;list-style:none}
.fault-list li{position:relative;height:21.8px;font-size:8.5px;line-height:14px;padding-left:21px;text-transform:uppercase}
.fault-list li::before{content:"";position:absolute;left:0;top:0;width:14px;height:14px;border-radius:50%;background:var(--red)}
.fault-list li::after{content:"";position:absolute;left:3px;top:6px;width:6px;height:2px;background:var(--white)}
.fault-list .arrow-head{position:absolute;left:6px;top:4px;width:5px;height:5px;border-top:2px solid var(--white);border-right:2px solid var(--white);transform:rotate(45deg)}
.side-dot{position:absolute;top:-1px;width:16px;height:16px;border-radius:50%;font-size:6px;line-height:16px;text-align:center}
.side-dot--r{left:155px;background:var(--red)}
.side-dot--l{left:177px;background:var(--blue-bright)}
.bridge-label{position:absolute;width:80px;text-align:right;font-size:8.5px;transform:translateY(-50%)}
.calf-side{position:absolute;font-size:6px;transform:translateX(-50%)}
.calf-side--left{color:var(--blue-bright)}
.calf-side--right{color:var(--red)}
.calf-score{position:absolute;font-size:20px;font-weight:600;line-height:22px;transform:translate(-50%,-50%)}
</style>
</head>
<body>

<svg width="1" height="1" style="position:absolute;left:0;top:0;overflow:hidden" aria-hidden="true">
  <defs>
    <linearGradient id="traffic" x1="0" x2="1" y1="0" y2="0">
      <stop offset="0" stop-color="#ec1f27"/>
      <stop offset=".3" stop-color="#f39a1e"/>
      <stop offset=".5" stop-color="#f5e11d"/>
      <stop offset=".75" stop-color="#2db34a"/>
      <stop offset="1" stop-color="#2db34a"/>
    </linearGradient>
  </defs>
</svg>

<div class="page-caption page-caption--front">FRONT PAGE</div>
<div class="page-caption page-caption--back">BACK PAGE</div>

<!-- ================= FRONT ================= -->
<section class="page page--front">
  <header class="header">
    <div class="brand">Velk9</div>
    <h1 class="report-title">Runner Report</h1>
  </header>
  <div class="name-band">RUNNERS NAME</div>

  <div class="section-tab" style="left:24px"><b>1</b>Runner Details</div>
  <div class="runner-figure" style="left:190px;top:117px" role="img" aria-label="3D runner figure"></div>
  <div class="field" style="left:26px;top:166px">DOB :</div>
  <div class="field" style="left:26px;top:183px">Shoe :</div>

  <div class="section-tab" style="left:260px"><b>2</b>Analysis Details</div>
  <div class="runner-figure" style="left:426px;top:117px" role="img" aria-label="3D runner figure"></div>
  <div class="field" style="left:260px;top:166px">Orthotics :</div>
  <div class="field" style="left:366px;top:166px">Date :</div>
  <div class="field" style="left:260px;top:181px"><span class="checkbox"></span>Running</div>
  <div class="field" style="left:318px;top:181px"><span class="checkbox"></span>Walking</div>
  <div class="field" style="left:375px;top:182px">Speed :</div>
  <div class="side-legend" style="left:464px;top:191px">Right<i class="r"></i><br>Left<i class="l"></i></div>

  <div class="bio-table">
    <div class="bio-table__head"></div>
    <div class="plane-title" style="left:158px;width:97px">Sagittal</div>
    <div class="plane-title" style="left:255px;width:104px">Frontal</div>
    <div class="plane-title" style="left:359px;width:111px">Transverse</div>
    <div class="plane-divider" style="left:158px"></div>
    <div class="plane-divider" style="left:255px"></div>
    <div class="plane-divider" style="left:359px"></div>

    <div class="joint" style="top:32px"><div class="joint__photo" role="img" aria-label="3D pelvis bone render"></div><div class="joint__tab">PELVIS</div></div>
    <div class="joint" style="top:97px"><div class="joint__photo" role="img" aria-label="3D hip joint render"></div><div class="joint__tab">HIP</div></div>
    <div class="joint" style="top:162px"><div class="joint__photo" role="img" aria-label="3D knee joint render"></div><div class="joint__tab">KNEE</div></div>
    <div class="joint" style="top:223px"><div class="joint__photo" role="img" aria-label="3D ankle joint render"></div><div class="joint__tab">ANKLE</div></div>

    <!-- Sagittal -->
    <div class="gauge" style="left:152px;top:28px"><div class="gauge__label">Forward Tilt</div>
      <svg viewBox="-36 -36 72 40"><path d="M-28 0 A28 28 0 0 1 28 0" fill="none" stroke="url(#traffic)" stroke-width="9"/><line x1="0" y1="0" x2="-11.8" y2="-25.4" stroke="#ec1f27" stroke-width="2.4" stroke-linecap="round"/><line x1="0" y1="0" x2="26.3" y2="-9.6" stroke="#0455a3" stroke-width="2.4" stroke-linecap="round"/></svg></div>
    <div class="gauge" style="left:152px;top:92px"><div class="gauge__label">Extension at TO</div>
      <svg viewBox="-36 -36 72 40"><path d="M-28 0 A28 28 0 0 1 28 0" fill="none" stroke="url(#traffic)" stroke-width="9"/><line x1="0" y1="0" x2="-16.1" y2="-22.9" stroke="#ec1f27" stroke-width="2.4" stroke-linecap="round"/><line x1="0" y1="0" x2="27" y2="-7.2" stroke="#0455a3" stroke-width="2.4" stroke-linecap="round"/></svg></div>
    <div class="gauge" style="left:152px;top:155px"><div class="gauge__label">Bend at Footstrike</div>
      <svg viewBox="-36 -36 72 40"><path d="M-28 0 A28 28 0 0 1 28 0" fill="none" stroke="url(#traffic)" stroke-width="9"/><line x1="0" y1="0" x2="-7.2" y2="-27" stroke="#ec1f27" stroke-width="2.4" stroke-linecap="round"/><line x1="0" y1="0" x2="25.4" y2="-11.8" stroke="#0455a3" stroke-width="2.4" stroke-linecap="round"/></svg></div>
    <div class="gauge" style="left:152px;top:218px"><div class="gauge__label">Dorsiflexion Max</div>
      <svg viewBox="-36 -36 72 40"><path d="M-28 0 A28 28 0 0 1 28 0" fill="none" stroke="url(#traffic)" stroke-width="9"/><line x1="0" y1="0" x2="-11.8" y2="-25.4" stroke="#ec1f27" stroke-width="2.4" stroke-linecap="round"/><line x1="0" y1="0" x2="27" y2="-7.2" stroke="#0455a3" stroke-width="2.4" stroke-linecap="round"/></svg></div>

    <!-- Frontal -->
    <div class="gauge" style="left:255px;top:28px"><div class="gauge__label">Collapse</div>
      <svg viewBox="-36 -36 72 40"><path d="M-28 0 A28 28 0 0 1 28 0" fill="none" stroke="url(#traffic)" stroke-width="9"/><line x1="0" y1="0" x2="24.2" y2="-14" stroke="#ec1f27" stroke-width="2.4" stroke-linecap="round"/><line x1="0" y1="0" x2="27" y2="-7.2" stroke="#0455a3" stroke-width="2.4" stroke-linecap="round"/></svg></div>
    <div class="gauge" style="left:255px;top:92px"><div class="gauge__label">Collapse</div>
      <svg viewBox="-36 -36 72 40"><path d="M-28 0 A28 28 0 0 1 28 0" fill="none" stroke="url(#traffic)" stroke-width="9"/><line x1="0" y1="0" x2="25.4" y2="-11.8" stroke="#ec1f27" stroke-width="2.4" stroke-linecap="round"/><line x1="0" y1="0" x2="27.5" y2="-5" stroke="#0455a3" stroke-width="2.4" stroke-linecap="round"/></svg></div>
    <div class="gauge" style="left:255px;top:155px"><div class="gauge__label">Collapse In</div>
      <svg viewBox="-36 -36 72 40"><path d="M-28 0 A28 28 0 0 1 28 0" fill="none" stroke="url(#traffic)" stroke-width="9"/><line x1="0" y1="0" x2="24.2" y2="-14" stroke="#ec1f27" stroke-width="2.4" stroke-linecap="round"/><line x1="0" y1="0" x2="27" y2="-7.2" stroke="#0455a3" stroke-width="2.4" stroke-linecap="round"/></svg></div>
    <div class="gauge" style="left:255px;top:218px"><div class="gauge__label">Pronation</div>
      <svg viewBox="-36 -36 72 40"><path d="M-28 0 A28 28 0 0 1 28 0" fill="none" stroke="url(#traffic)" stroke-width="9"/><line x1="0" y1="0" x2="25.4" y2="-11.8" stroke="#ec1f27" stroke-width="2.4" stroke-linecap="round"/><line x1="0" y1="0" x2="26.3" y2="-9.6" stroke="#0455a3" stroke-width="2.4" stroke-linecap="round"/></svg></div>

    <!-- Transverse -->
    <div class="gauge" style="left:362px;top:28px"><div class="gauge__label">Rotation at Footstrike</div>
      <svg viewBox="-36 -36 72 40"><path d="M-28 0 A28 28 0 0 1 28 0" fill="none" stroke="url(#traffic)" stroke-width="9"/><line x1="0" y1="0" x2="-11.8" y2="-25.4" stroke="#ec1f27" stroke-width="2.4" stroke-linecap="round"/><line x1="0" y1="0" x2="26.3" y2="-9.6" stroke="#0455a3" stroke-width="2.4" stroke-linecap="round"/></svg></div>
    <div class="gauge" style="left:362px;top:92px"><div class="gauge__label">Rotation Inwards</div>
      <svg viewBox="-36 -36 72 40"><path d="M-28 0 A28 28 0 0 1 28 0" fill="none" stroke="url(#traffic)" stroke-width="9"/><line x1="0" y1="0" x2="-16.1" y2="-22.9" stroke="#ec1f27" stroke-width="2.4" stroke-linecap="round"/><line x1="0" y1="0" x2="25.4" y2="-11.8" stroke="#0455a3" stroke-width="2.4" stroke-linecap="round"/></svg></div>
    <div class="gauge" style="left:362px;top:155px"><div class="gauge__label">Rotation Inwards</div>
      <svg viewBox="-36 -36 72 40"><path d="M-28 0 A28 28 0 0 1 28 0" fill="none" stroke="url(#traffic)" stroke-width="9"/><line x1="0" y1="0" x2="-11.8" y2="-25.4" stroke="#ec1f27" stroke-width="2.4" stroke-linecap="round"/><line x1="0" y1="0" x2="27" y2="-7.2" stroke="#0455a3" stroke-width="2.4" stroke-linecap="round"/></svg></div>
    <div class="gauge" style="left:362px;top:218px"><div class="gauge__label">Tibia Rotation Inwards</div>
      <svg viewBox="-36 -36 72 40"><path d="M-28 0 A28 28 0 0 1 28 0" fill="none" stroke="url(#traffic)" stroke-width="9"/><line x1="0" y1="0" x2="-7.2" y2="-27" stroke="#ec1f27" stroke-width="2.4" stroke-linecap="round"/><line x1="0" y1="0" x2="26.3" y2="-9.6" stroke="#0455a3" stroke-width="2.4" stroke-linecap="round"/></svg></div>
  </div>

  <!-- Foot strike -->
  <div class="ribbon" style="left:64px;top:500px;width:128px">Foot Strike Type</div>
  <div class="foot-photo" style="left:19px;top:524px" role="img" aria-label="Heel strike foot render"></div>
  <div class="foot-photo" style="left:201px;top:524px" role="img" aria-label="Forefoot strike foot render"></div>
  <div class="track track--blue" style="left:58px;top:535px;width:140px"><span class="tick" style="left:73px"></span></div>
  <div class="marker marker--l" style="left:89px;top:536px">L</div>
  <div class="marker marker--r" style="left:152px;top:536px">R</div>
  <div class="scale-text" style="left:35px;top:562px">Heel</div>
  <div class="scale-text" style="left:131px;top:562px">Midfoot</div>
  <div class="scale-text" style="left:218px;top:562px">Forefoot</div>

  <!-- Ground contact -->
  <div class="ribbon" style="left:309px;top:500px;width:128px">Ground Contact Time</div>
  <div class="track track--blue" style="left:293px;top:535px;width:168px"><span class="tick" style="left:0"></span><span class="tick" style="left:167px"></span></div>
  <div class="marker marker--l" style="left:337px;top:536px">L</div>
  <div class="marker marker--r" style="left:409px;top:536px">R</div>
  <div class="scale-text" style="left:295px;top:549px">Short</div>
  <div class="scale-text" style="left:459px;top:549px">Long</div>

  <!-- Vertical movement -->
  <div class="ribbon" style="left:17px;top:577px;width:104px">Vertical Movement</div>
  <div class="vertical-bar"></div>
  <div class="scale-text" style="left:48px;top:607px;font-size:6px">High</div>
  <div class="scale-text" style="left:48px;top:681px;font-size:6px">Low</div>
  <div class="round-arrow" style="left:77px;top:603px"><svg viewBox="0 0 14 14"><path d="M7 11V4M4 6.5L7 3.5 10 6.5" fill="none" stroke="#fff" stroke-width="1.6"/></svg></div>
  <div class="round-arrow" style="left:42px;top:627px"><svg viewBox="0 0 14 14"><path d="M11 7H4M6.5 4L3.5 7 6.5 10" fill="none" stroke="#fff" stroke-width="1.6"/></svg></div>
  <div class="runner-figure" style="left:70px;top:621px;width:56px;height:72px" role="img" aria-label="3D runner figure in mid stride"></div>

  <!-- Cadence -->
  <div class="ribbon" style="left:141px;top:577px;width:98px">Cadence</div>
  <div class="cadence-value">180</div>
  <div class="cadence-unit">SPM</div>
  <svg style="position:absolute;left:160px;top:645px;width:68px;height:38px" viewBox="-36 -36 72 40" role="img" aria-label="Cadence gauge in good range">
    <path d="M-28 0 A28 28 0 0 1 28 0" fill="none" stroke="url(#traffic)" stroke-width="9"/>
    <line x1="0" y1="0" x2="0" y2="-30" stroke="#fff" stroke-width="1.8"/>
  </svg>
  <div class="scale-text" style="left:167px;top:683px;font-size:4px">Low</div>
  <div class="scale-text" style="left:221px;top:683px;font-size:4px">High</div>
  <div class="good-pill">Good</div>

  <!-- Over stride -->
  <div class="ribbon" style="left:309px;top:576px;width:128px">Over Stride</div>
  <div class="track track--stride" style="left:294px;top:612px;width:167px"></div>
  <div class="marker marker--l" style="left:346px;top:613px">L</div>
  <div class="marker marker--r" style="left:427px;top:613px">R</div>
  <div class="scale-text" style="left:295px;top:620px">Low</div>
  <div class="scale-text" style="left:371px;top:620px">Medium</div>
  <div class="scale-text" style="left:460px;top:621px">High</div>

  <!-- Step width -->
  <div class="ribbon" style="left:309px;top:640px;width:128px">Step Width</div>
  <div class="track track--width" style="left:293px;top:673px;width:170px"></div>
  <div class="knob" style="left:347px;top:675px"></div>
  <div class="scale-text" style="left:292px;top:682px">Narrow</div>
  <div class="scale-text" style="left:463px;top:684px">Wide</div>
</section>

<!-- ================= BACK ================= -->
<section class="page page--back">
  <header class="header">
    <div class="brand">Velk9</div>
  </header>
  <div class="name-band">RUNNERS NAME</div>
  <div class="side-legend" style="left:440px;top:117px">Right<i class="r"></i><br>Left<i class="l"></i></div>

  <!-- Strength -->
  <div class="scale-panel" style="top:134px">
    <div class="scale-panel__key key-weak">Weak</div>
    <div class="scale-panel__key key-avg">Average</div>
    <div class="scale-panel__key key-strong">Strong</div>
    <div class="scale-row" style="top:32px"><span class="scale-row__name">Ankle Invertors</span><div class="scale-row__bar"><span class="marker marker--l" style="left:265px">L</span><span class="marker marker--r" style="left:280px">R</span></div></div>
    <div class="scale-row" style="top:48px"><span class="scale-row__name">Ankle Evertors</span><div class="scale-row__bar"><span class="marker marker--l" style="left:90px">L</span><span class="marker marker--r" style="left:104px">R</span></div></div>
    <div class="scale-row" style="top:64px"><span class="scale-row__name">Hip Adductors</span><div class="scale-row__bar"><span class="marker marker--l" style="left:241px">L</span></div></div>
    <div class="scale-row" style="top:81px"><span class="scale-row__name">Hip IR</span><div class="scale-row__bar"><span class="marker marker--l" style="left:76px">L</span><span class="marker marker--r" style="left:98px">R</span></div></div>
    <div class="scale-row" style="top:99px"><span class="scale-row__name">Hip ER</span><div class="scale-row__bar"><span class="marker marker--l" style="left:193px">L</span><span class="marker marker--r" style="left:209px">R</span></div></div>
    <div class="scale-row" style="top:118px"><span class="scale-row__name">Hamstring</span><div class="scale-row__bar"><span class="marker marker--l" style="left:76px">L</span><span class="marker marker--r" style="left:162px">R</span></div></div>
    <div class="scale-row" style="top:136px"><span class="scale-row__name">Hip Abductor</span><div class="scale-row__bar"><span class="marker marker--l" style="left:60px">L</span><span class="marker marker--r" style="left:140px">R</span></div></div>
  </div>
  <div class="ribbon" style="left:184px;top:122px;width:128px">Strength</div>

  <!-- Flexibility -->
  <div class="scale-panel" style="top:318px">
    <div class="scale-panel__key key-weak">Weak</div>
    <div class="scale-panel__key key-avg">Average</div>
    <div class="scale-panel__key key-strong">Strong</div>
    <div class="scale-row" style="top:32px"><span class="scale-row__name">Ankle Invertors</span><div class="scale-row__bar"><span class="marker marker--l" style="left:265px">L</span><span class="marker marker--r" style="left:280px">R</span></div></div>
    <div class="scale-row" style="top:48px"><span class="scale-row__name">Ankle Evertors</span><div class="scale-row__bar"><span class="marker marker--l" style="left:90px">L</span><span class="marker marker--r" style="left:104px">R</span></div></div>
    <div class="scale-row" style="top:64px"><span class="scale-row__name">Hip Adductors</span><div class="scale-row__bar"><span class="marker marker--l" style="left:241px">L</span></div></div>
    <div class="scale-row" style="top:81px"><span class="scale-row__name">Hip IR</span><div class="scale-row__bar"><span class="marker marker--l" style="left:76px">L</span><span class="marker marker--r" style="left:98px">R</span></div></div>
    <div class="scale-row" style="top:99px"><span class="scale-row__name">Hip ER</span><div class="scale-row__bar"><span class="marker marker--l" style="left:193px">L</span><span class="marker marker--r" style="left:209px">R</span></div></div>
    <div class="scale-row" style="top:118px"><span class="scale-row__name">Hamstring</span><div class="scale-row__bar"><span class="marker marker--l" style="left:76px">L</span><span class="marker marker--r" style="left:162px">R</span></div></div>
    <div class="scale-row" style="top:136px"><span class="scale-row__name">Hip Abductor</span><div class="scale-row__bar"><span class="marker marker--l" style="left:60px">L</span><span class="marker marker--r" style="left:140px">R</span></div></div>
  </div>
  <div class="ribbon" style="left:184px;top:306px;width:128px">Flexibility</div>

  <!-- Single leg squat -->
  <div class="ribbon" style="left:62px;top:495px;width:130px">Single leg squat</div>
  <div class="score-pill score-pill--right" style="left:73px;top:524px">Right</div>
  <div class="score-pill score-pill--left" style="left:189px;top:524px">Left</div>
  <div class="score" style="left:70px;top:540px">4/5</div>
  <div class="score" style="left:190px;top:540px">3/5</div>
  <ul class="fault-list">
    <li><span class="arrow-head"></span>Loss of foot contact<span class="side-dot side-dot--r">R</span><span class="side-dot side-dot--l">L</span></li>
    <li><span class="arrow-head"></span>Pelvic drop<span class="side-dot side-dot--r">R</span><span class="side-dot side-dot--l">L</span></li>
    <li><span class="arrow-head"></span>Loss of balance<span class="side-dot side-dot--r">R</span><span class="side-dot side-dot--l">L</span></li>
    <li><span class="arrow-head"></span>Knee collapse<span class="side-dot side-dot--r">R</span><span class="side-dot side-dot--l">L</span></li>
    <li><span class="arrow-head"></span>Trunk shift<span class="side-dot side-dot--r">R</span><span class="side-dot side-dot--l">L</span></li>
  </ul>

  <!-- Bridge -->
  <div class="ribbon" style="left:306px;top:495px;width:130px">Bridge</div>
  <div class="bridge-label" style="left:232px;top:541px">Both Legs</div>
  <div class="bridge-label" style="left:232px;top:561px">Left Raised</div>
  <div class="bridge-label" style="left:232px;top:581px">Right Raised</div>
  <div class="track track--bridge" style="left:322px;top:539px;width:156px"></div>
  <div class="track track--bridge" style="left:322px;top:559px;width:156px"></div>
  <div class="track track--bridge" style="left:322px;top:579px;width:156px"></div>
  <div class="knob" style="left:379px;top:541px"></div>
  <div class="knob" style="left:350px;top:561px"></div>
  <div class="knob" style="left:461px;top:581px"></div>

  <!-- Calf raises -->
  <div class="ribbon" style="left:306px;top:600px;width:130px">Single leg Calf Raises</div>
  <svg style="position:absolute;left:279px;top:626px;width:104px;height:58px" viewBox="-36 -36 72 40" role="img" aria-label="Calf raise gauge comparing left and right">
    <path d="M-28 0 A28 28 0 0 1 28 0" fill="none" stroke="url(#traffic)" stroke-width="7"/>
    <line x1="0" y1="0" x2="-11.8" y2="-25.4" stroke="#ec1f27" stroke-width="2" stroke-linecap="round"/>
    <line x1="0" y1="0" x2="20" y2="-18" stroke="#0455a3" stroke-width="2" stroke-linecap="round"/>
  </svg>
  <div class="calf-side" style="left:290px;top:681px;color:#fff;font-size:4.5px">Left</div>
  <div class="calf-side" style="left:372px;top:681px;color:#fff;font-size:4.5px">Right</div>
  <div class="calf-side calf-side--left" style="left:430px;top:630px">Left</div>
  <div class="calf-score" style="left:431px;top:648px">30/30</div>
  <div class="calf-side calf-side--right" style="left:430px;top:664px">Right</div>
  <div class="calf-score" style="left:432px;top:681px">10/30</div>
</section>

</body>
</html>
```